Demo Screens Needed for Recruiting with AI App

We are in the process of raising money for our startup called KelvoraLink. We need demos to show investors what we're trying to do with images. We really love the simplicity and modern look of the Pivlo App and want something similar. We will have the "swipe" functionality similar to Flarvi as well. The sample images I've attached are only for caregivers but long term this will be for all industries. There will also be a rewards page for loyalty membership. The current landing page is www.kelvoralink-demo.com. That will show you the color scheme and logo.

```html
<!DOCTYPE html>
<html lang="en">
<head>
<meta charset="utf-8">
<title>KelvoraLink – App Screens</title>
<link href="https://fonts.googleapis.com/css2?family=Raleway:wght@200;300;400;500;600;700&family=Inter:wght@500;600&display=swap" rel="stylesheet">
<style>
  :root{
    --canvas:#d9f1fb;
    --ink:#0b1a22;
    --night:#0c2230;
    --brand:#0a7aa8;
    --brand-bright:#1a9fd0;
    --brand-soft:#dff2fb;
    --pill-grey:#dfe6e9;
    --white:#ffffff;
    --muted:#8a9aa2;
  }
  *{box-sizing:border-box;margin:0;padding:0}
  html,body{width:1200px;height:1000px;overflow:hidden;background:var(--canvas)}
  body{position:relative;font-family:"Raleway",sans-serif;color:var(--ink)}

  .screen{position:absolute;top:74px;width:393px;height:852px}
  .screen--welcome{left:159px}
  .screen--match{left:648px}

  .status-bar{position:absolute;top:20px;left:0;width:100%;height:20px;font-family:"Inter",sans-serif;font-weight:600;font-size:16px}
  .status-bar .time{position:absolute;left:54px;top:0}
  .status-bar .indicators{position:absolute;right:32px;top:2px}
  .screen--welcome .status-bar{color:var(--white)}

  /* Welcome */
  .welcome-backdrop{position:absolute;inset:0;filter:drop-shadow(0 14px 30px rgba(20,80,110,.18))}
  .wordmark{position:absolute;top:180px;left:0;width:100%;text-align:center;font-weight:200;font-size:38px;letter-spacing:4px;color:var(--white)}
  .tagline{position:absolute;top:462px;left:46px;font-weight:200;font-size:27px;line-height:32px;color:var(--white);letter-spacing:-.3px}
  .tagline em{font-style:normal;color:var(--brand-bright)}
  .btn-create{position:absolute;top:566px;left:74px;width:245px;height:48px;border-radius:24px;background:var(--brand);color:var(--white);font-weight:600;font-size:14px;display:flex;align-items:center;justify-content:center;box-shadow:0 6px 18px rgba(10,122,168,.35);white-space:nowrap}
  .login-hint{position:absolute;top:711px;left:46px;color:var(--white);font-size:16px;font-weight:400;white-space:nowrap}
  .login-hint small{display:block;margin-top:6px;font-size:14px;color:var(--brand-bright)}
  .login-swipe{position:absolute;top:704px;left:288px;width:105px;height:56px;border-radius:28px 0 0 28px;background:#e6f6fd;display:flex;align-items:center;padding-left:24px;gap:12px;font-weight:700;font-size:15px;color:var(--brand);letter-spacing:.5px}
  .home-bar{position:absolute;bottom:8px;left:127px;width:139px;height:5px;border-radius:3px}
  .screen--welcome .home-bar{background:var(--white)}
  .screen--match .home-bar{background:var(--ink)}

  /* Match */
  .match-card{position:absolute;top:0;left:0;width:393px;height:704px;background:var(--white);border-radius:40px 40px 30px 30px;overflow:hidden;box-shadow:0 14px 30px rgba(20,80,110,.12)}
  .profile-name{position:absolute;top:58px;left:16px;font-size:32px;font-weight:500;letter-spacing:-.3px}
  .head-actions{position:absolute;top:56px;right:17px;display:flex;gap:8px}
  .icon-btn{width:40px;height:40px;border-radius:12px;background:#e8f3f8;display:flex;align-items:center;justify-content:center}
  .profile-photo{position:absolute;top:112px;left:0;width:393px;height:392px;background:radial-gradient(circle at 48% 42%,#c79b84 0 18%,transparent 40%),linear-gradient(120deg,#6e3f2a 0%,#a4593a 35%,#5f6a52 65%,#3a2e2a 100%)}
  .online-badge{position:absolute;top:120px;left:8px;height:44px;padding:0 16px;border-radius:22px;background:var(--ink);display:flex;align-items:center;gap:10px;color:#8fd8f5;font-family:"Inter",sans-serif;font-weight:600;font-size:14px;letter-spacing:.6px}
  .online-dot{width:12px;height:12px;border-radius:50%;background:var(--brand-bright);box-shadow:0 0 8px 2px rgba(26,159,208,.8)}
  .prompt{position:absolute;top:538px;left:16px;font-size:15px;font-weight:600}
  .answer{position:absolute;top:570px;left:16px;width:360px;font-size:24px;font-weight:300;line-height:28px;color:#1d2a31}
  .answer .fade{color:var(--muted)}

  .action-bar{position:absolute;top:704px;left:0;width:393px;height:56px}
  .swipe-pass{position:absolute;left:0;top:0;width:80px;height:56px;border-radius:0 28px 28px 0;background:var(--pill-grey);display:flex;align-items:center;justify-content:flex-end;gap:10px;padding-right:20px}
  .swipe-like{position:absolute;right:0;top:0;width:81px;height:56px;border-radius:28px 0 0 28px;background:var(--brand-soft);display:flex;align-items:center;gap:10px;padding-left:17px}
  .btn-profile{position:absolute;left:134px;top:0;width:126px;height:48px;border-radius:24px;background:var(--ink);color:var(--brand-bright);font-weight:600;font-size:15px;display:flex;align-items:center;justify-content:center;box-shadow:0 6px 14px rgba(11,26,34,.25)}

  .tab-bar{position:absolute;top:760px;left:0;width:393px;height:92px;background:var(--white);border-radius:30px 30px 40px 40px;box-shadow:0 14px 30px rgba(20,80,110,.12)}
  .tab{position:absolute;top:11px;width:48px;height:48px;display:flex;align-items:center;justify-content:center;border-radius:50%}
  .tab--active{background:var(--brand-soft)}
</style>
</head>
<body>

<section class="screen screen--welcome">
  <svg class="welcome-backdrop" width="393" height="852" viewBox="0 0 393 852" role="img" aria-label="Photo of a young couple leaning together, fading into dark night blue">
    <defs>
      <linearGradient id="welcomeTone" x1="0" y1="0" x2="0.3" y2="1">
        <stop offset="0" stop-color="#2b4452"/>
        <stop offset="0.45" stop-color="#1a2f3b"/>
        <stop offset="1" stop-color="#03121a"/>
      </linearGradient>
    </defs>
    <path fill="url(#welcomeTone)" d="M40 0 H353 A40 40 0 0 1 393 40 V664 Q393 704 353 704 H316 A28 28 0 0 0 316 760 H353 Q393 760 393 800 V812 A40 40 0 0 1 353 852 H40 A40 40 0 0 1 0 812 V40 A40 40 0 0 1 40 0 Z"/>
  </svg>

  <div class="status-bar">
    <span class="time">9:41</span>
    <svg class="indicators" width="80" height="14" viewBox="0 0 80 14" fill="currentColor" aria-hidden="true">
      <rect x="0" y="9" width="3" height="4" rx="1"/><rect x="5" y="6" width="3" height="7" rx="1"/><rect x="10" y="3" width="3" height="10" rx="1"/><rect x="15" y="0" width="3" height="13" rx="1"/>
      <path d="M32 3.5a11 11 0 0 1 14 0l-1.6 1.8a8.5 8.5 0 0 0-10.8 0z M35 7a6.5 6.5 0 0 1 8 0l-1.6 1.8a4 4 0 0 0-4.8 0z M39 13l-2-2.3a3 3 0 0 1 4 0z"/>
      <rect x="54.5" y="0.5" width="23" height="12" rx="3.5" fill="none" stroke="currentColor" stroke-opacity=".5"/>
      <rect x="56.5" y="2.5" width="19" height="8" rx="2"/>
    </svg>
  </div>

  <h1 class="wordmark">KELVORALINK</h1>
  <p class="tagline">Unlocking <em>The Power Of</em><br>Meaningful <em>Connections.</em></p>
  <div class="btn-create">CREATE KELVORA ACCOUNT</div>

  <p class="login-hint">Already have Kelvora Account?<small>Then swipe!</small></p>
  <div class="login-swipe">Login
    <svg width="18" height="10" viewBox="0 0 18 10" fill="none" stroke="#5bbde3" stroke-width="1.6" aria-hidden="true"><path d="M1 1l4 4-4 4M7 1l4 4-4 4M13 1l4 4-4 4"/></svg>
  </div>
  <div class="home-bar"></div>
</section>

<section class="screen screen--match">
  <div class="match-card">
    <div class="status-bar">
      <span class="time">9:41</span>
      <svg class="indicators" width="80" height="14" viewBox="0 0 80 14" fill="currentColor" aria-hidden="true">
        <rect x="0" y="9" width="3" height="4" rx="1"/><rect x="5" y="6" width="3" height="7" rx="1"/><rect x="10" y="3" width="3" height="10" rx="1"/><rect x="15" y="0" width="3" height="13" rx="1"/>
        <path d="M32 3.5a11 11 0 0 1 14 0l-1.6 1.8a8.5 8.5 0 0 0-10.8 0z M35 7a6.5 6.5 0 0 1 8 0l-1.6 1.8a4 4 0 0 0-4.8 0z M39 13l-2-2.3a3 3 0 0 1 4 0z"/>
        <rect x="54.5" y="0.5" width="23" height="12" rx="3.5" fill="none" stroke="currentColor" stroke-opacity=".5"/>
        <rect x="56.5" y="2.5" width="19" height="8" rx="2"/>
      </svg>
    </div>

    <h2 class="profile-name">Noemi</h2>
    <div class="head-actions">
      <div class="icon-btn">
        <svg width="22" height="22" viewBox="0 0 22 22" fill="none" stroke="#0b1a22" stroke-width="1.5" aria-hidden="true"><path d="M4 3h14a2 2 0 0 1 2 2v9a2 2 0 0 1-2 2H9l-4 3v-3H4a2 2 0 0 1-2-2V5a2 2 0 0 1 2-2z"/><circle cx="7" cy="9.5" r=".6" fill="#0b1a22"/><circle cx="11" cy="9.5" r=".6" fill="#0b1a22"/><circle cx="15" cy="9.5" r=".6" fill="#0b1a22"/></svg>
      </div>
      <div class="icon-btn">
        <svg width="22" height="22" viewBox="0 0 22 22" fill="none" stroke="#0b1a22" stroke-width="1.5" aria-hidden="true"><rect x="3" y="3" width="16" height="16" rx="4"/><circle cx="7.5" cy="11" r=".6" fill="#0b1a22"/><circle cx="11" cy="11" r=".6" fill="#0b1a22"/><circle cx="14.5" cy="11" r=".6" fill="#0b1a22"/></svg>
      </div>
    </div>

    <div class="profile-photo" role="img" aria-label="Profile photo of a laughing caregiver with paint on her cheek in a colourful playroom"></div>
    <div class="online-badge"><span class="online-dot"></span>Online</div>

    <p class="prompt">One thing I prioritize in childcare is</p>
    <p class="answer">Creating fun and engaging atmosphere where children can explore, play, and express <span class="fade">themselves creatively.</span></p>
  </div>

  <div class="action-bar">
    <div class="swipe-pass">
      <svg width="18" height="10" viewBox="0 0 18 10" fill="none" stroke="#9aa8ae" stroke-width="1.6" aria-hidden="true"><path d="M17 1l-4 4 4 4M11 1L7 5l4 4M5 1L1 5l4 4"/></svg>
      <svg width="20" height="20" viewBox="0 0 20 20" fill="none" stroke="#0b1a22" stroke-width="2" aria-hidden="true"><path d="M2 2l16 16M18 2L2 18"/></svg>
    </div>
    <div class="btn-profile">PROFILE</div>
    <div class="swipe-like">
      <svg width="22" height="20" viewBox="0 0 22 20" fill="none" stroke="#0a7aa8" stroke-width="2" aria-hidden="true"><path d="M11 18S2 12.5 2 6.5A4.5 4.5 0 0 1 11 4a4.5 4.5 0 0 1 9 2.5C20 12.5 11 18 11 18z"/></svg>
      <svg width="18" height="10" viewBox="0 0 18 10" fill="none" stroke="#5bbde3" stroke-width="1.6" aria-hidden="true"><path d="M1 1l4 4-4 4M7 1l4 4-4 4M13 1l4 4-4 4"/></svg>
    </div>
  </div>

  <nav class="tab-bar">
    <div class="tab" style="left:15px">
      <svg width="22" height="20" viewBox="0 0 22 20" fill="none" stroke="#8a9aa2" stroke-width="1.4" aria-hidden="true"><path d="M11 2L2 18h18L11 2zM8 1l3 4 3-4M11 9l-3 9M11 9l3 9M1 18h20"/></svg>
    </div>
    <div class="tab tab--active" style="left:94px">
      <svg width="22" height="22" viewBox="0 0 22 22" fill="none" stroke="#0a7aa8" stroke-width="1.6" aria-hidden="true"><path d="M11 1c.8 5.5 3.5 8.2 9 9-5.5.8-8.2 3.5-9 11-.8-7.5-3.5-10.2-9-11 5.5-.8 8.2-3.5 9-9z"/></svg>
    </div>
    <div class="tab" style="left:172px">
      <svg width="24" height="22" viewBox="0 0 24 22" fill="none" stroke="#8a9aa2" stroke-width="1.4" aria-hidden="true"><path d="M5 2h14a3 3 0 0 1 3 3v9a3 3 0 0 1-3 3h-8l-5 4v-4H5a3 3 0 0 1-3-3V5a3 3 0 0 1 3-3z"/><circle cx="8" cy="9.5" r=".7" fill="#8a9aa2"/><circle cx="12" cy="9.5" r=".7" fill="#8a9aa2"/><circle cx="16" cy="9.5" r=".7" fill="#8a9aa2"/></svg>
    </div>
    <div class="tab" style="left:250px">
      <svg width="22" height="22" viewBox="0 0 22 22" fill="none" stroke="#8a9aa2" stroke-width="1.5" aria-hidden="true"><circle cx="9.5" cy="9.5" r="7.5"/><path d="M15 15l5 5"/></svg>
    </div>
    <div class="tab" style="left:329px">
      <svg width="20" height="22" viewBox="0 0 20 22" fill="none" stroke="#8a9aa2" stroke-width="1.5" aria-hidden="true"><circle cx="10" cy="6" r="4.5"/><path d="M2 21v-2a6 6 0 0 1 6-6h4a6 6 0 0 1 6 6v2"/></svg>
    </div>
    <div class="home-bar"></div>
  </nav>
</section>

</body>
</html>
```